DLB / WLB

I need a business card for the owner of sister companies. Please see minimalist version of our old business card for just the Dalworth business. We need to now have a card that shows off both the Dalworth logo and the Willow Lane Builders logo. We would like the aesthetic to go well with our brand, and not differ greatly from our Dalworth cards. These companies are sister companies, there is not one parent company. Looking for a visually appealing design, but not sure if it should be diagonal or something to make it visually attractive... or just some other type of divider. We prefer white logos with a blue background. White transparent background png logos are attached. Please use blue background with hex code 566b7c. The person and contact information will be on the back side, and I can do that myself. We will NOT need to add the text for design-build-sales-installation.

```html
<!DOCTYPE html>
<html lang="en">
<head>
<meta charset="utf-8">
<title>Dalworth + Willow Lane Builders — Business Card</title>
<link href="https://fonts.googleapis.com/css2?family=Poppins:wght@400;500;600;700&display=swap" rel="stylesheet">
<style>
  :root {
    --card-blue: #566b7c;
    --ink-white: #ffffff;
    --backdrop: #e6e8ea;
    --divider: rgba(255, 255, 255, 0.85);
  }
  * { margin: 0; padding: 0; box-sizing: border-box; }
  html, body { width: 1200px; height: 1200px; overflow: hidden; }
  body {
    background: var(--backdrop);
    font-family: "Poppins", sans-serif;
    color: var(--ink-white);
    position: relative;
  }
  .card {
    position: absolute;
    left: 227px;
    width: 746px;
    height: 438px;
    background: var(--card-blue);
    border-radius: 22px;
  }
  .card--front { top: 148px; }
  .card--back { top: 614px; }

  .divider {
    position: absolute;
    width: 1.5px;
    background: var(--divider);
  }
  .card--front .divider { left: 372px; top: 112px; height: 234px; }
  .card--back .divider { left: 376px; top: 179px; height: 230px; }

  .brand {
    position: absolute;
    display: flex;
    flex-direction: column;
    align-items: center;
    text-align: center;
    transform: translateX(-50%);
  }
  .brand__square { background: var(--ink-white); }
  .brand__name { font-weight: 600; line-height: 1.15; letter-spacing: 0.01em; }

  .card--front .brand { top: 150px; }
  .card--front .brand--dalworth { left: 207px; }
  .card--front .brand--willow { left: 546px; }
  .card--front .brand__square { width: 62px; height: 62px; margin-bottom: 26px; }
  .card--front .brand__name { font-size: 27px; }

  .holder-name {
    position: absolute;
    top: 50px; left: 0; right: 0;
    text-align: center;
    font-weight: 500;
    font-size: 46px;
    letter-spacing: 0.01em;
  }
  .holder-title {
    position: absolute;
    top: 113px; left: 0; right: 0;
    text-align: center;
    font-weight: 400;
    font-size: 17px;
    letter-spacing: 0.03em;
  }

  .card--back .brand { top: 190px; }
  .card--back .brand--dalworth { left: 203px; }
  .card--back .brand--willow { left: 560px; }
  .card--back .brand__square { width: 34px; height: 34px; margin-bottom: 12px; }
  .card--back .brand__name { font-size: 15px; }

  .contact {
    position: absolute;
    top: 308px;
    display: flex;
    flex-direction: column;
    align-items: center;
    transform: translateX(-50%);
    white-space: nowrap;
  }
  .contact--dalworth { left: 190px; }
  .contact--willow { left: 562px; }
  .contact__phone { font-weight: 700; font-size: 37px; line-height: 1.1; }
  .contact__line { font-weight: 600; font-size: 17.5px; line-height: 1.45; }
</style>
</head>
<body>
  <section class="card card--front" aria-label="Card front">
    <div class="brand brand--dalworth">
      <div class="brand__square"></div>
      <p class="brand__name">dalworth+co<br>kitchen+bath</p>
    </div>
    <div class="divider"></div>
    <div class="brand brand--willow">
      <div class="brand__square"></div>
      <p class="brand__name">willow lane<br>builders</p>
    </div>
  </section>

  <section class="card card--back" aria-label="Card back">
    <h1 class="holder-name">EVAN R. DALWORTH</h1>
    <p class="holder-title">MANAGING DIRECTOR</p>

    <div class="brand brand--dalworth">
      <div class="brand__square"></div>
      <p class="brand__name">dalworth+co<br>kitchen+bath</p>
    </div>
    <div class="divider"></div>
    <div class="brand brand--willow">
      <div class="brand__square"></div>
      <p class="brand__name">willow lane<br>builders</p>
    </div>

    <div class="contact contact--dalworth">
      <p class="contact__phone">555-014-2231</p>
      <p class="contact__line">evan@dalworthco.com</p>
      <p class="contact__line">www.dalworthco.com</p>
    </div>
    <div class="contact contact--willow">
      <p class="contact__phone">555-014-2217</p>
      <p class="contact__line">evan@willowlanebuilders.com</p>
      <p class="contact__line">www.willowlanebuilders.com</p>
    </div>
  </section>
</body>
</html>
```